Refresh of a Media Kit for Adtech Company - Needs jazzing up!

We have a Media Kit that's too ugly and boring to send to clients. Attaching some examples of ones we like better. Keep the general styling and theme of the current media kit (it's our brand style) and all the information conveyed, but please change anything and everything else to make it more dynamic. Attaching examples of media kits we like.

The "Media Kit Vexa" is the one you're designing, the others are just examples of media kits we liked.
Updates

Here's a link to "Glamour Shots" that can be used as appropriate throughout the Media kit: https://www.filecrate-example.com/sh/k8trw21mzpq4xnb/QXP7Lmv3bRw8_TzKe4jHsUcYd?dl=0

Target Market(s)

Demand partners

Colors
0592cd
85cae6
34a7d8

Requirements
Nice to have
• Here are some glamour shots you can use if you see a good fit for any of them: https://www.filecrate-example.com/sh/k8trw21mzpq4xnb/QXP7Lmv3bRw8_TzKe4jHsUcYd?dl=0

```html
<!DOCTYPE html>
<html lang="en">
<head>
<meta charset="utf-8">
<title>Vexa Media Kit — Overview</title>
<link href="https://fonts.googleapis.com/css2?family=Roboto:wght@300;400;500;700&display=swap" rel="stylesheet">
<style>
:root{
  --page:#e6e6e6;
  --hero:#0890fd;
  --brand:#0592cd;
  --brand-light:#85cae6;
  --brand-mid:#34a7d8;
  --accent:#1a8cf0;
  --ink:#2b2b2b;
  --muted:#555;
  --rule:#d9d9d9;
  --gray-bar:#b9b9b9;
  --white:#fff;
}
*{margin:0;padding:0;box-sizing:border-box}
html,body{width:1200px;height:724px;overflow:hidden;background:var(--page);font-family:'Roboto',Arial,sans-serif;color:var(--ink)}
.canvas{position:relative;width:1200px;height:724px}
.slide{position:absolute;width:544px;height:306px;background:var(--white);overflow:hidden}
.s1{left:39px;top:40px;background:var(--hero)}
.s2{left:617px;top:40px}
.s3{left:39px;top:377px}
.s4{left:617px;top:377px}
.abs{position:absolute}
.page-num{position:absolute;right:12px;bottom:4px;font-size:38px;font-weight:700;color:#9a9a9a}

.hero-title{left:57px;top:112px;font-size:20.5px;line-height:24.5px;font-weight:300;color:var(--white)}
.hero-title b{font-weight:700}
.hero-bar{left:58px;top:208px;width:137px;height:5px;background:#5cb6fb}

.headline{font-size:15px;line-height:20px;font-weight:300;color:var(--ink)}
.headline b{font-weight:700}
.label{font-size:10px;font-weight:300;color:var(--ink)}
.label b{font-weight:700}
.uline{height:2px;width:36px;background:var(--brand-light)}
.vrule{width:1px;background:var(--rule)}

.map{left:22px;top:150px;width:170px;height:90px;background:linear-gradient(160deg,#e4e4e4,#cfcfcf);border-radius:18px 30px 22px 40px}
.stats{left:185px;top:140px;width:70px;text-align:center}
.stat{margin-bottom:7px}
.stat-num{font-size:10px;font-weight:700;color:var(--accent);line-height:12px}
.stat-cap{font-size:6px;color:var(--muted);line-height:7.5px}

.footer{position:absolute;top:290px;display:flex;align-items:center;gap:18px}
.dooh{font-size:7px;letter-spacing:4.5px;color:var(--accent)}
.brand-name{display:flex;align-items:center;gap:3px;font-size:7.5px;font-weight:700;color:var(--accent)}
.brand-name i{display:block;width:8px;height:8px;background:var(--accent);border-radius:2px}

.photo{left:280px;top:0;width:264px;height:306px;background:linear-gradient(90deg,rgba(255,255,255,1) 0%,rgba(220,222,224,.6) 35%,#b7babd 70%,#9ea2a6 100%)}
.aud-col{font-size:7px;color:var(--muted);text-align:center;line-height:8.5px}
.partner{font-size:10px;font-weight:700;color:#222;line-height:12px;white-space:nowrap}
.footer.on-photo .dooh,.footer.on-photo .brand-name{color:var(--white)}
.footer.on-photo .brand-name i{background:var(--white)}

.globe{left:0;top:0;width:125px;height:306px;background:radial-gradient(circle at 0% 45%,#eef3f8 0%,#dde8f2 55%,#ffffff 100%)}
.feat{width:86px;font-size:6.6px;color:var(--muted);line-height:8.6px}
.feat h3{font-size:7px;font-weight:700;color:var(--ink);line-height:8.5px;margin:0 0 9px}
.feat ul{list-style:none;padding-left:7px}
.feat li{position:relative}
.feat li::before{content:"";position:absolute;left:-6px;top:3px;width:2px;height:2px;background:var(--accent)}
.feat .sub{padding-left:12px}
.icon-circle{width:33px;height:33px;border-radius:50%;background:var(--accent);display:flex;align-items:center;justify-content:center;margin:0 0 13px 10px}
.tagline{font-size:10px;font-weight:300;color:var(--ink);text-align:center;line-height:12px;width:90px}
</style>
</head>
<body>
<div class="canvas">

  <!-- Slide 1: hero -->
  <section class="slide s1">
    <h1 class="abs hero-title">Vexa’s platform <b>unlocks DOOH</b><br>for your brands and advertisers,<br>programmatically, at scale.</h1>
    <div class="abs hero-bar"></div>
  </section>

  <!-- Slide 2: reach -->
  <section class="slide s2">
    <h2 class="abs headline" style="left:22px;top:30px;width:480px"><b>REACH;</b> Vexa is your DOOH partner, connecting your partners and advertisers to a nation-wide network of place-based screens.</h2>
    <div class="abs label" style="left:22px;top:104px">Our network, <b>today</b></div>
    <div class="abs uline" style="left:23px;top:121px"></div>
    <div class="abs map" role="img" aria-label="Map of the United States with network venue locations"></div>
    <div class="abs stats">
      <div class="stat"><div class="stat-num">23B+</div><div class="stat-cap">Impressions<br>Annually</div></div>
      <div class="stat"><div class="stat-num">50</div><div class="stat-cap">DMA’s</div></div>
      <div class="stat"><div class="stat-num">55,105+</div><div class="stat-cap">Venues</div></div>
      <div class="stat"><div class="stat-num">61,410+</div><div class="stat-cap">Screens</div></div>
    </div>
    <div class="abs vrule" style="left:255px;top:103px;height:150px"></div>
    <div class="abs label" style="left:268px;top:104px">Our network, <b>soon</b></div>
    <div class="abs uline" style="left:269px;top:121px"></div>

    <svg class="abs" style="left:265px;top:125px" width="270" height="135" viewBox="0 0 270 135" font-family="Roboto, Arial, sans-serif">
      <text x="8" y="75" font-size="4" font-weight="700" fill="#444" transform="rotate(-90 8 75)">DIGITAL SIGNS</text>
      <g stroke="#ccc" stroke-width=".5" stroke-dasharray="1.5 1.5">
        <line x1="16.5" y1="10" x2="16.5" y2="104"/><line x1="35.5" y1="10" x2="35.5" y2="104"/>
        <line x1="54.5" y1="10" x2="54.5" y2="104"/><line x1="73.5" y1="10" x2="73.5" y2="104"/>
        <line x1="92.5" y1="10" x2="92.5" y2="104"/><line x1="111.5" y1="10" x2="111.5" y2="104"/>
        <line x1="130.5" y1="10" x2="130.5" y2="104"/><line x1="149.5" y1="10" x2="149.5" y2="104"/>
        <line x1="168.5" y1="10" x2="168.5" y2="104"/>
      </g>
      <g stroke-width="3" stroke-linecap="round">
        <line x1="18" y1="97.6" x2="33" y2="97.6" stroke="#d0d0d0"/>
        <line x1="37" y1="94.2" x2="52" y2="94.2" stroke="#d0d0d0"/>
        <line x1="56" y1="85.4" x2="71" y2="85.4" stroke="#d0d0d0"/>
        <line x1="75" y1="82" x2="90" y2="82" stroke="#d0d0d0"/>
        <line x1="94" y1="72.2" x2="109" y2="72.2" stroke="var(--gray-bar)"/>
        <line x1="113" y1="67.4" x2="128" y2="67.4" stroke="var(--gray-bar)"/>
        <line x1="132" y1="63.5" x2="147" y2="63.5" stroke="var(--gray-bar)"/>
        <line x1="151" y1="58.6" x2="166" y2="58.6" stroke="var(--gray-bar)"/>
        <line x1="170" y1="51.3" x2="185" y2="51.3" stroke="var(--accent)"/>
        <line x1="189" y1="40.6" x2="204" y2="40.6" stroke="var(--accent)"/>
        <line x1="208" y1="35.7" x2="223" y2="35.7" stroke="var(--accent)"/>
        <line x1="227" y1="26" x2="242" y2="26" stroke="var(--accent)"/>
      </g>
      <g font-size="4.2" fill="#666" text-anchor="middle">
        <text x="25" y="121" dy="-28">100</text>
        <text x="44" y="88">250</text>
        <text x="63" y="80">800</text>
        <text x="82" y="76">1,000</text>
        <text x="101" y="66">48,500</text>
        <text x="120" y="61">55,000</text>
        <text x="139" y="57">70,000</text>
        <text x="158" y="52">106,000</text>
        <text x="177" y="45">135,000</text>
        <text x="196" y="34">181,000</text>
        <text x="215" y="30">203,000</text>
        <text x="234" y="19">251,000</text>
      </g>
      <g transform="translate(168.5 17)">
        <path d="M0 -9 a3.5 3.5 0 0 1 3.5 3.5 c0 2.5 -3.5 6 -3.5 6 s-3.5 -3.5 -3.5 -6 a3.5 3.5 0 0 1 3.5 -3.5z" fill="var(--accent)"/>
        <circle cx="0" cy="-5.5" r="1.3" fill="#fff"/>
        <text x="0" y="6" font-size="4.2" font-weight="700" fill="var(--accent)" text-anchor="middle">Today</text>
      </g>
      <g font-size="2.8" fill="#fff" text-anchor="middle" font-weight="700">
        <circle cx="16.5" cy="106" r="3.2" fill="#c6c6c6"/><circle cx="35.5" cy="106" r="3.2" fill="#c6c6c6"/>
        <circle cx="54.5" cy="106" r="3.2" fill="#c6c6c6"/><circle cx="73.5" cy="106" r="3.2" fill="#c6c6c6"/>
        <circle cx="92.5" cy="106" r="3.2" fill="#9a9a9a"/><circle cx="111.5" cy="106" r="3.2" fill="#9a9a9a"/>
        <circle cx="130.5" cy="106" r="3.2" fill="#9a9a9a"/><circle cx="149.5" cy="106" r="3.2" fill="#9a9a9a"/>
        <circle cx="168.5" cy="106" r="3.2" fill="var(--accent)"/><circle cx="187.5" cy="106" r="3.2" fill="var(--accent)"/>
        <circle cx="206.5" cy="106" r="3.2" fill="var(--accent)"/><circle cx="225.5" cy="106" r="3.2" fill="var(--accent)"/>
        <text x="16.5" y="107">Q1</text><text x="35.5" y="107">Q2</text><text x="54.5" y="107">Q3</text><text x="73.5" y="107">Q4</text>
        <text x="92.5" y="107">Q1</text><text x="111.5" y="107">Q2</text><text x="130.5" y="107">Q3</text><text x="149.5" y="107">Q4</text>
        <text x="168.5" y="107">Q1</text><text x="187.5" y="107">Q2</text><text x="206.5" y="107">Q3</text><text x="225.5" y="107">Q4</text>
      </g>
      <rect x="16" y="112" width="76" height="2.5" rx="1.2" fill="#d4d4d4"/>
      <rect x="92" y="112" width="76" height="2.5" rx="1.2" fill="#9a9a9a"/>
      <rect x="168" y="112" width="76" height="2.5" rx="1.2" fill="var(--accent)"/>
      <g font-size="5" font-weight="700" fill="#333" text-anchor="middle">
        <text x="16.5" y="125">2019</text><text x="92.5" y="125">2020</text>
        <text x="168.5" y="125">2021</text><text x="244" y="125">2022</text>
      </g>
    </svg>

    <div class="footer" style="left:407px"><span class="dooh">DOOH NOW</span><span class="brand-name"><i></i>Vexa</span></div>
  </section>

  <!-- Slide 3: audience -->
  <section class="slide s3">
    <div class="abs photo" role="img" aria-label="Blurred aerial view of commuters walking through a busy station concourse"></div>
    <h2 class="abs headline" style="left:23px;top:29px;width:390px"><b>Audience;</b> Vexa’s network exposes your advertisers’ messaging to a large, varied, unique set of audiences.</h2>

    <div class="abs label" style="left:32px;top:94px"><b>Audiences...</b></div>
    <div class="abs uline" style="left:32px;top:109px"></div>
    <div class="abs aud-col" style="left:27px;top:123px;width:50px">
      <svg width="26" height="26" viewBox="0 0 26 26" fill="none" stroke="var(--accent)" stroke-width="1.4"><circle cx="17" cy="5" r="3"/><path d="M13 24V12a4 4 0 0 1 8 0v12"/><circle cx="8" cy="11" r="5.5"/><path d="M8 8v6M6.5 9.5h3"/></svg>
      <div>High net<br>worth</div>
    </div>
    <div class="abs aud-col" style="left:27px;top:178px;width:50px">
      <svg width="26" height="22" viewBox="0 0 26 22" fill="none" stroke="var(--accent)" stroke-width="1.4"><rect x="2" y="3" width="22" height="15"/><line x1="13" y1="3" x2="13" y2="18"/><circle cx="13" cy="10.5" r="3"/><rect x="2" y="7" width="4" height="7"/><rect x="20" y="7" width="4" height="7"/></svg>
      <div>Sports Fans</div>
    </div>
    <div class="abs aud-col" style="left:75px;top:185px;width:45px">And many<br>more</div>
    <div class="abs aud-col" style="left:27px;top:220px;width:50px">
      <svg width="26" height="26" viewBox="0 0 26 26" fill="none" stroke="var(--accent)" stroke-width="1.4"><circle cx="8" cy="5" r="2.5"/><path d="M6 9l1 8h6l3 7M4 12v8h6"/><circle cx="19" cy="8" r="4.5"/><path d="M19 6v2.5h2"/></svg>
      <div>High dwell<br>time</div>
    </div>

    <div class="abs vrule" style="left:125px;top:93px;height:175px"></div>
    <div class="abs label" style="left:135px;top:93px;line-height:13px">...you can buy<br><b>anywhere...</b></div>
    <div class="abs uline" style="left:135px;top:122px"></div>
    <div class="abs" style="left:137px;top:136px">
      <div class="partner" style="margin-bottom:9px">Quillra</div>
      <div class="partner" style="margin-bottom:9px">Hexmarket</div>
      <div class="partner" style="margin-bottom:9px">Signwave</div>
      <div class="partner" style="margin-bottom:9px">Rondel</div>
      <div class="partner" style="margin-bottom:9px">AdMatrix</div>
      <div class="partner" style="margin-bottom:9px">Veridon Media</div>
      <div class="partner">Venue Exchange</div>
    </div>

    <div class="abs vrule" style="left:223px;top:93px;height:175px"></div>
    <div class="abs label" style="left:233px;top:92px">...however <b>you’d like.</b></div>
    <div class="abs uline" style="left:233px;top:108px"></div>
    <div class="abs aud-col" style="left:230px;top:123px;width:50px">
      <svg width="26" height="26" viewBox="0 0 26 26" fill="none" stroke="var(--accent)" stroke-width="1.4"><path d="M5 20L13 3l8 17z"/><circle cx="13" cy="14" r="3"/><path d="M3 23h20"/></svg>
      <div>Open RTD</div>
    </div>
    <div class="abs aud-col" style="left:224px;top:167px;width:62px">
      <svg width="26" height="26" viewBox="0 0 26 26" fill="none" stroke="var(--accent)" stroke-width="1.4"><circle cx="13" cy="13" r="3"/><circle cx="4" cy="4" r="2.5"/><circle cx="22" cy="4" r="2.5"/><circle cx="4" cy="22" r="2.5"/><circle cx="22" cy="22" r="2.5"/><path d="M6 6l5 5M20 6l-5 5M6 20l5-5M20 20l-5-5"/></svg>
      <div>Programmatic<br>Guaranteed</div>
    </div>
    <div class="abs aud-col" style="left:224px;top:222px;width:62px">
      <svg width="26" height="26" viewBox="0 0 26 26" fill="none" stroke="var(--accent)" stroke-width="1.4"><rect x="4" y="3" width="18" height="12"/><circle cx="10" cy="9" r="2.5"/><path d="M13 15v8M9 23h8"/></svg>
      <div>Private<br>Marketplace</div>
    </div>

    <div class="footer on-photo" style="left:407px"><span class="dooh">DOOH NOW</span><span class="brand-name"><i></i>Vexa</span></div>
  </section>

  <!-- Slide 4: performance -->
  <section class="slide s4">
    <div class="abs globe" role="img" aria-label="Wireframe globe of connected network points"></div>
    <h2 class="abs headline" style="left:139px;top:28px;width:380px">technology and seamless integration delivers class-leading <b>campaign</b> performance.</h2>

    <div class="abs feat" style="left:157px;top:82px">
      <div class="icon-circle"><svg width="16" height="16" viewBox="0 0 16 16" fill="none" stroke="#fff" stroke-width="1.2"><rect x="2" y="2" width="9" height="10"/><circle cx="6" cy="7" r="2"/><circle cx="12" cy="12" r="2.5"/></svg></div>
      <h3>Fast, functional<br>integration</h3>
      <ul><li>Have our inventory available to your clients in 4 weeks, in time for end of Covid</li></ul>
      <div style="margin-top:4px">3 integration paths:</div>
      <ul class="sub"><li>openRTB</li><li>VAST tags</li><li>or a Custom API</li></ul>
    </div>
    <div class="abs vrule" style="left:246px;top:82px;height:190px"></div>
    <div class="abs feat" style="left:252px;top:82px">
      <div class="icon-circle"><svg width="16" height="16" viewBox="0 0 16 16" fill="none" stroke="#fff" stroke-width="1.2"><circle cx="6" cy="10" r="3.5"/><circle cx="6" cy="10" r="1.2"/><circle cx="11.5" cy="4.5" r="2.5"/></svg></div>
      <h3>Reliable, High<br>Performance Inventory</h3>
      <ul><li>100% fill rate</li><li>Quality controlled</li><li>Honest viewability reporting</li></ul>
    </div>
    <div class="abs vrule" style="left:341px;top:82px;height:190px"></div>
    <div class="abs feat" style="left:346px;top:82px">
      <div class="icon-circle"><svg width="16" height="16" viewBox="0 0 16 16" fill="none" stroke="#fff" stroke-width="1.2"><path d="M2 8l6-6h6v6l-6 6z"/><circle cx="10" cy="10" r="3" fill="var(--accent)"/><path d="M10 8.5v3"/></svg></div>
      <h3 style="margin-bottom:17px">Lower CPM’S</h3>
      <ul><li>$6 avg. on Vexa</li><li>$9-32 elsewhere —often for the same screens</li></ul>
    </div>
    <div class="abs vrule" style="left:433px;top:82px;height:190px"></div>
    <div class="abs feat" style="left:439px;top:82px">
      <div class="icon-circle"><svg width="16" height="16" viewBox="0 0 16 16" fill="none" stroke="#fff" stroke-width="1.2"><path d="M2 14h12M4 14V9M7 14V7M10 14V9M13 14V5"/><path d="M3 6l4-3 3 2 4-3"/></svg></div>
      <h3>Robust<br>Analytics</h3>
      <ul><li>X screens with Tallyscreen technology</li><li>Rest have x type of analytics</li></ul>
    </div>

    <div class="abs tagline" style="left:138px;top:251px">Up and running<br>in no time!</div>
    <div class="abs tagline" style="left:233px;top:251px">Budgets will<br>spend!</div>
    <div class="abs tagline" style="left:335px;top:251px">Budgets will go<br>further!</div>
    <div class="abs tagline" style="left:420px;top:251px">More data!</div>

    <div class="footer" style="left:407px"><span class="dooh">DOOH NOW</span><span class="brand-name"><i></i>Vexa</span></div>
  </section>

  <div class="page-num">2</div>
</div>
</body>
</html>
```